coaching agenda

Please redesign the brochure attached in a more modern/trendy out look. I want something completely different to what is attached but using the same colours and logo.

```html
<!DOCTYPE html>
<html lang="en">
<head>
<meta charset="utf-8">
<title>Coaching Session – June 2018</title>
<link href="https://fonts.googleapis.com/css2?family=Roboto+Condensed:wght@300;400;700&family=Roboto:wght@400;500;700&display=swap" rel="stylesheet">
<style>
  :root{
    --stage:#8f8f8f;
    --paper:#ffffff;
    --ink:#2b2b2b;
    --ink-soft:#3d3d3d;
    --grey-head:#a3a3a3;
    --teal:#0b7fa8;
    --teal-deep:#0a6a8f;
    --sky:#29abe2;
    --label-dark:#3a3a3a;
  }
  *{margin:0;padding:0;box-sizing:border-box}
  html,body{width:1200px;height:878px;overflow:hidden}
  body{background:var(--stage);position:relative;font-family:"Roboto",Arial,sans-serif;color:var(--ink)}
  .page{position:absolute;top:58px;width:515px;height:730px;background:var(--paper)}
  .page--front{left:67px}
  .page--back{left:619px}
  .abs{position:absolute}

  /* brand */
  .brand{position:absolute;display:flex;flex-direction:column;align-items:flex-start}
  .brand__mark{width:34px;height:34px;background:var(--ink);margin-bottom:6px}
  .brand__name{font-family:"Roboto",sans-serif;font-size:13px;font-weight:400;color:var(--ink)}
  .brand__sub{font-size:4.6px;color:#666;margin-top:1px}
  .brand--small .brand__mark{width:22px;height:22px;margin-bottom:3px;background:var(--teal)}
  .brand--small .brand__name{font-size:7px}
  .brand--small .brand__sub{font-size:3px}

  /* header banner */
  .banner{left:159px;top:14px;width:356px;height:77px;border-radius:14px 0 0 14px;
    background:linear-gradient(90deg,var(--teal) 0%,var(--teal-deep) 100%);color:#fff;text-align:center;
    font-family:"Roboto Condensed",sans-serif}
  .banner__title{font-size:35px;font-weight:700;margin-top:11px;line-height:1;letter-spacing:.3px}
  .banner__date{font-size:21px;font-weight:300;letter-spacing:4px;margin-top:6px;line-height:1}

  .headline{left:12px;top:106px;width:494px;text-align:center;font-family:"Roboto Condensed",sans-serif;
    font-weight:700;font-size:35px;color:var(--grey-head);letter-spacing:.2px;line-height:1}

  .question-box{left:37px;top:147px;width:442px;height:57px;border:1px dashed var(--sky);border-radius:6px;
    text-align:center;font-size:9.6px;font-weight:500;line-height:12.4px;padding-top:3px;color:var(--ink)}

  .rule{position:absolute;height:1px;background:var(--ink)}
  .rule--sky{background:var(--sky)}

  .label{position:absolute;font-family:"Roboto Condensed",sans-serif;font-weight:700;color:#fff;text-align:center;white-space:nowrap}
  .label--dark{background:var(--label-dark);border-radius:3px}
  .label--sky{background:var(--sky)}

  .subhead{font-family:"Roboto Condensed",sans-serif;font-weight:700;color:var(--sky);text-align:center;font-size:15.5px}

  /* checklists */
  .checks{list-style:none;position:absolute}
  .checks li{position:relative;padding-left:11px;font-size:7.4px;line-height:9.3px;color:var(--ink-soft)}
  .checks li::before{content:"";position:absolute;left:0;top:1.5px;width:6px;height:6px;border:1px solid var(--sky)}
  .checks li::after{content:"";position:absolute;left:2px;top:1.8px;width:2.5px;height:4.2px;
    border-right:1.2px solid var(--sky);border-bottom:1.2px solid var(--sky);transform:rotate(40deg)}
  .checks--gap li{margin-bottom:9.5px}
  .checks--tight li{margin-bottom:2.8px}
  .checks--list li{margin-bottom:1.1px}
  .checks--big li{font-size:11.5px;line-height:13.7px;padding-left:16px;color:var(--ink)}
  .checks--big li::before{top:3px;width:8px;height:8px}
  .checks--big li::after{left:2.8px;top:3.3px;width:3px;height:5.5px}

  .intro{left:0;top:482px;width:515px;text-align:center;font-size:7.4px;font-weight:700;line-height:9.4px;color:var(--ink)}

  .prose{font-size:7px;line-height:8.8px;color:var(--ink-soft)}
  .prose p{margin-bottom:8.6px}
  .prose--domain p{margin-bottom:7px}
  .prose--domain strong{font-weight:400;font-size:8.6px;color:var(--ink)}

  /* year badges */
  .year{position:absolute;width:80px;margin-left:-40px;text-align:center}
  .year__disc{width:38px;height:38px;margin:0 auto;border-radius:50%;background:var(--teal);
    border:2px dotted var(--sky);outline:1px solid var(--sky);color:#fff;font-family:"Roboto Condensed",sans-serif;
    font-weight:700;font-size:11px;line-height:34px}
  .year__word{font-family:"Roboto Condensed",sans-serif;font-weight:700;font-size:14.5px;margin-top:5px;color:var(--ink)}
</style>
</head>
<body>

<section class="page page--front" aria-label="Coaching session agenda, front">
  <div class="brand" style="left:26px;top:22px">
    <span class="brand__mark"></span>
    <span class="brand__name">Dalton Reeve</span>
    <span class="brand__sub">Salesguide Partners Pty Ltd</span>
  </div>

  <header class="banner abs">
    <div class="banner__title">COACHING SESSION</div>
    <div class="banner__date">JUNE 2018</div>
  </header>

  <h1 class="headline abs">YESTERDAY–TODAY–TOMORROW</h1>

  <div class="question-box abs">
    How many appraisals/listing presentations are booked in your diary for this week?<br>
    How many appraisals/listing presentations are booked in your diary for next week?<br>
    How many second viewings/private viewings are booked in your diary for this week?<br>
    How many listings will you launch this week?
  </div>

  <div class="rule" style="left:79px;top:235px;width:358px"></div>
  <div class="label label--dark" style="left:125px;top:223px;width:266px;height:25px;font-size:16px;line-height:25px">2018/2019 PRODUCTIVITY GETS</div>
  <div class="subhead abs" style="left:0;top:253px;width:515px">THERE’S MORE TO IT THAN NUMBERS</div>

  <ul class="checks checks--gap" style="left:18px;top:281px;width:232px">
    <li>Increase in market share in your core area</li>
    <li>Increase in commission rates</li>
    <li>Relationships [ data base growth]- future sellers</li>
    <li>Relationships [ data base growth] – buyer prospects</li>
    <li>Number of appointments/appraisals booked each week</li>
    <li>Listing pipeline growth</li>
    <li>Skills development –is an opportunity - you can’t be defined as not knowing what to do. Be specific. You can’t become a better closer if you don’t have people to close on!!</li>
    <li>Managing free time – you can’t be defined by time</li>
  </ul>

  <ul class="checks checks--gap" style="left:266px;top:281px;width:240px">
    <li>Time is an opportunity</li>
    <li>Know your data base system – data base is an opportunity</li>
    <li>Service charter – there is opportunity in service – repeat/referrals/the future seller calls “you in”</li>
    <li>Health &amp; energy leads to better recovery</li>
    <li>Family &amp; self- breaks</li>
    <li>Self-time</li>
    <li style="margin-top:10px">Milestones/benchmarks</li>
    <li style="margin-top:12px">Wealth creation</li>
  </ul>

  <div class="rule rule--sky" style="left:79px;top:461px;width:358px"></div>
  <div class="label label--sky" style="left:142px;top:450px;width:232px;height:21px;font-size:16px;line-height:21px">TODAY ONWARDS [12/6/18]</div>

  <p class="intro abs">
    Build the listing pipeline so you have shock coming to market when the sun shines again<br>
    Don’t wait until the usual “spring selling session” promo’s start to start looking for listings.<br>
    Get the &nbsp;jump on your competition by having your July to December profile building campaign set in place now &amp; make sure it is<br>
    fully funded so you don’t lose profile momentum.
  </p>

  <ul class="checks" style="left:18px;top:533px;width:480px">
    <li style="margin-bottom:9.4px">What went well this month?</li>
    <li style="margin-bottom:9.4px">Did you convert good days into good weeks, good weeks into a good month?</li>
    <li style="margin-bottom:9.4px">How organised were you last week?</li>
    <li style="margin-bottom:9.4px">What ideas, actions, processes, systems and motivations have you introduced into your business during the last thirty days?</li>
    <li style="margin-bottom:9.4px">What systems do you need to implement to create a smoother work flow?</li>
    <li style="margin-bottom:9.4px">Are you pursuing what you believe in?</li>
    <li style="margin-bottom:9.4px">At what time of the day are you running at your true potential?</li>
    <li style="margin-bottom:9.4px">What have been your numbers for May?</li>
    <li>Script session – what was the best script you used last week?</li>
  </ul>
</section>

<section class="page page--back" aria-label="Coaching session agenda, back">
  <ul class="checks checks--tight" style="left:50px;top:23px;width:190px">
    <li>Speak to’s</li>
    <li>Appointments</li>
    <li>Appraisals</li>
    <li>Listing presentations</li>
    <li>Listing pipeline</li>
    <li>Listing authorities signed</li>
  </ul>
  <ul class="checks checks--tight" style="left:259px;top:20px;width:230px">
    <li>Listings launched</li>
    <li>Home opens</li>
    <li>Negotiations</li>
    <li>Sales</li>
    <li>Lessons learned list</li>
    <li>Inroads into the market share in your core area – are &nbsp;you competitive, you when you are being called in</li>
  </ul>

  <div class="label label--sky" style="left:142px;top:121px;width:232px;height:20px;font-size:15.5px;line-height:20px">BUILD AN AUDIENCE</div>

  <div class="prose abs" style="left:17px;top:152px;width:468px">
    <p>All real estate sales people have customers. Lucky ones have fans. But the most fortunate real estate sales people have audiences. An audience can be your point of difference.</p>
    <p>A lot of real estate people still spend big bucks to reach people. Every time they want to say something, they dip into their marketing budgets, pull out some cash and do some “marketing”. This approach is both expensive and unreliable. As has been said, you waste half of your marketing budget, you just don’t know which half.</p>
    <p>Today’s smart real estate sales person knows better. Instead of going out to reach people, you want people to come to you. An audience returns often – on its own – to see what you have to say. This is the most receptive group of prospective customers and customers you’ll ever have.</p>
  </div>

  <ul class="checks checks--big" style="left:90px;top:258px">
    <li>Send</li><li>Say</li><li>Connect</li><li>Capture</li>
  </ul>
  <ul class="checks checks--big" style="left:229px;top:258px">
    <li>Connect</li><li>Present</li><li>Convert</li><li>List</li>
  </ul>
  <ul class="checks checks--big" style="left:369px;top:256px">
    <li style="font-size:13px;margin-bottom:4.5px">Market</li>
    <li style="font-size:13px;margin-bottom:4.5px">Sell</li>
    <li style="font-size:13px">Retain</li>
  </ul>

  <div class="label label--sky" style="left:114px;top:324px;width:287px;height:21px;font-size:16px;line-height:21px">MAKE THE UNCOMMON COMMON</div>

  <ul class="checks" style="left:17px;top:358px;width:470px">
    <li style="margin-bottom:4px">Time – no time is no excuse – you cannot be defined by time in 2018/ the need to do more for less following the industry discounting of fees.</li>
    <li style="margin-bottom:4px">How you manage free time</li>
    <li style="margin-bottom:4px">You cannot be defined by not knowing what to do</li>
    <li>Embrace where your market is at:</li>
  </ul>

  <div class="year" style="left:82px;top:427px"><div class="year__disc">2015</div><div class="year__word">WOW</div></div>
  <div class="year" style="left:178px;top:427px"><div class="year__disc">2016</div><div class="year__word">HOPE</div></div>
  <div class="year" style="left:294px;top:427px"><div class="year__disc">2017</div><div class="year__word">NEW NORM</div></div>
  <div class="year" style="left:414px;top:427px"><div class="year__disc">2017</div><div class="year__word">THE NORM</div></div>

  <div class="label label--sky" style="left:62px;top:500px;width:392px;height:20px;font-size:16px;line-height:20px">WHAT ARE YOUR BEHAVIOURS COSTING YOU</div>

  <div class="prose prose--domain abs" style="left:13px;top:540px;width:480px">
    <p><strong>PUBLIC DOMAIN</strong> – those areas where people see you acting on your behaviours, both positive &amp; negative. Professionalism, application, integrity, self-esteem, respect for others &nbsp;&amp; proficiency are on display here</p>
    <p><strong>PRIVATE DOMAIN</strong> – is the one where we spend time with ourselves &amp; where our mind games play out. This is the biggest behavioural &nbsp;game of all as we confront out habits, limitations, acceptance of disruptions, temptations &amp; fears</p>
  </div>

  <ul class="checks checks--list" style="left:15px;top:601px;width:300px">
    <li>Know your CRM system</li>
    <li>Capture data &amp; use it to generate an income</li>
    <li>Buyer work</li>
    <li>6 weeks after settlement</li>
    <li>Significantly increase the number of “just listed” you drop</li>
    <li>Put a name to a property</li>
  </ul>

  <div class="brand brand--small" style="left:452px;top:672px">
    <span class="brand__mark"></span>
    <span class="brand__name">Dalton Reeve</span>
    <span class="brand__sub">Salesguide Partners Pty Ltd</span>
  </div>
</section>

</body>
</html>
```